VELMIQ Business Presentation Powerpoint

We need a powerpoint template based around our logo/coloursThe powerpoint will be used for 1. business development (sales)2. presentation of reports etc

Looking for snappy ways of presenting data (findings) - graphs, tabulations etc

Target Market(s)

Banks, multinational developers, construction groups
CEO, COO, VP, EGM etc

Industry/Entity Type

Consultant

Colors
3277b5

Requirements
Must have
• Main title page
• Standard Title page
• Tabulations style page
• Listing style page
• Graph style page
• Image with text box (2 on a page) style page
• Essentally all features used in business
Nice to have
• Pie chart style page
• open to amy presentation ideas

```html
<!DOCTYPE html>
<html lang="en">
<head>
<meta charset="utf-8">
<title>VELMIQ Business Presentation</title>
<link href="https://fonts.googleapis.com/css2?family=Montserrat:wght@400;600;700;800&family=Open+Sans:wght@300;400;600;700&family=Roboto:wght@700&display=swap" rel="stylesheet">
<style>
:root{
  --navy:#0b4677;
  --blue:#1f5fa6;
  --accent:#3277b5;
  --ink:#23232b;
  --muted:#77777f;
  --tile:#e8e6ec;
  --page:#f3f4f6;
  --bar-a:#3a6ab3;
  --bar-b:#3d3a3e;
  --bar-c:#2f8ad6;
}
*{margin:0;padding:0;box-sizing:border-box}
html,body{width:720px;height:1200px;overflow:hidden}
body{position:relative;background:var(--page);font-family:"Open Sans",sans-serif;color:var(--ink)}

.side-band{position:absolute;left:0;top:0;width:298px;height:1200px;background:var(--navy)}

.features{position:absolute;left:0;top:0;width:298px;height:393px;color:#fff;font-family:"Roboto",sans-serif;font-weight:700}
.feat{position:absolute;left:45px;font-size:16px;line-height:1;white-space:nowrap}
.feat.box::before{content:"";position:absolute;left:-25px;top:-3px;width:15px;height:15px;border:2px solid #fff;border-radius:2px}
.feat.sub{left:66px}
.feat.sub::before{content:"";position:absolute;left:-13px;top:3px;width:6px;height:6px;background:#fff}
.feat.sub2{left:77px}
.feat.sub2::before{content:"";position:absolute;left:-22px;top:3px;width:6px;height:6px;background:#fff}
.feat.light{font-family:"Open Sans",sans-serif;font-weight:400}
.feat.cont{left:42px}

.cover{position:absolute;left:337px;top:64px;width:366px;height:206px;overflow:hidden;box-shadow:0 2px 8px rgba(0,0,0,.2)}
.cover-top{position:absolute;left:0;top:0;width:366px;height:124px;background:linear-gradient(120deg,#e9eef4 0%,#b9c8da 45%,#6d86a3 75%,#d8e0ea 100%)}
.cover-band{position:absolute;left:0;top:124px;width:366px;height:41px;background:var(--navy)}
.cover-name{position:absolute;right:14px;top:131px;color:#fff;font:800 19px "Montserrat",sans-serif;letter-spacing:.5px}
.cover-bottom{position:absolute;left:0;top:165px;width:366px;height:41px;background:linear-gradient(100deg,#dfe6ef 0%,#8fb0d6 40%,#3f78bf 70%,#e4eaf2 100%)}

.slide{position:absolute;width:226px;height:127px;background:#fff;overflow:hidden;box-shadow:0 1px 3px rgba(0,0,0,.18)}
.r1{top:394px}.r2{top:529px}.r3{top:663px}.r4{top:798px}.r5{top:932px}.r6{top:1067px}
.c1{left:6px}.c2{left:247px}.c3{left:487px}

.brand{position:absolute;top:6px;right:10px;font:800 7px "Montserrat",sans-serif;color:var(--ink);letter-spacing:.3px}
.brand.left{left:21px;right:auto}
.pg{position:absolute;left:0;bottom:0;width:17px;height:9px;background:#f1f1f3;font-size:3px;color:#999;text-align:center;line-height:9px}
.tick{position:absolute;left:6px;top:63px;width:7px;height:1px;background:#999}

.title{position:absolute;font-family:"Montserrat",sans-serif;font-weight:700;line-height:1;color:var(--ink)}
.title .hl{color:var(--blue)}
.subtitle{position:absolute;font:700 5px "Open Sans",sans-serif;color:var(--ink)}
.para{position:absolute;font-size:3px;line-height:1.45;color:var(--muted)}
.para b{color:var(--ink)}
.photo{position:absolute;background:linear-gradient(135deg,#d7dde4,#8e9db0)}
.photo.blue{background:linear-gradient(135deg,#bcd3ec,#2d6db5)}
.photo.warm{background:linear-gradient(135deg,#e2ddd6,#9a8f85)}
.photo.dark{background:linear-gradient(135deg,#8aa0b8,#27384d)}
.navy-block{position:absolute;background:var(--navy)}
.navy-block .arrow{position:absolute;right:4px;bottom:4px;width:6px;height:1px;background:#fff}

.agenda-band{position:absolute;left:95px;top:74px;width:131px;height:9px;background:#e9e7ed}
.agenda-num{position:absolute;top:77px;font-size:2.5px;color:#777}
.col-head{position:absolute;font:600 5.5px "Open Sans",sans-serif;color:var(--ink)}

.circle{position:absolute;border-radius:50%;background:#ececef;box-shadow:1px 2px 3px rgba(0,0,0,.25);text-align:center}
.circle .yr{display:block;font:700 5.5px "Open Sans",sans-serif;margin-top:12px}
.circle .note{display:block;font-size:2px;color:#888;padding:0 5px;line-height:1.3}

.strat-box{position:absolute;width:46px;height:46px;background:var(--tile);border-top:1px solid var(--navy);padding:5px 4px}
.strat-box h4{font:600 3.5px "Open Sans",sans-serif;margin-bottom:2px}
.strat-box p{font-size:2.3px;line-height:1.4;color:var(--muted)}
.icon-box{position:absolute;width:46px;height:46px;background:#f4f4f6;border-top:1px solid var(--navy);text-align:center;padding-top:10px;box-shadow:0 1px 2px rgba(0,0,0,.12)}
.icon-box svg{display:block;margin:0 auto 5px}
.icon-box h4{font:600 3.2px "Open Sans",sans-serif;color:var(--ink)}
.icon-box p{font-size:2.2px;color:var(--muted);padding:1px 4px 0}

.meter{position:absolute;left:21px;width:76px;height:9px;background:#eceaef}
.meter span{position:absolute;left:0;top:0;height:9px;background:#bfbcc4;font-size:2.5px;color:#fff;line-height:9px;padding-left:3px}
.meter em{position:absolute;top:0;font-style:normal;font:700 4px "Open Sans",sans-serif;color:#fff;line-height:9px}
.meter.active span{background:var(--navy)}

.member{position:absolute;top:43px;width:38px}
.member .portrait{width:38px;height:52px;background:linear-gradient(160deg,#c8ccd2,#5d636c)}
.member .name{font:700 3.5px "Open Sans",sans-serif;margin-top:3px;padding-left:1px}
.member .role{font-size:2.3px;color:#888;padding-left:1px}
.member.lead .caption{background:var(--navy);color:#fff;padding:1px 2px 2px;margin-top:0}
.member.lead .caption .name{margin-top:1px}
.member.lead .caption .role{color:#cfe0f0}
</style>
</head>
<body>

<div class="side-band"></div>

<div class="features">
  <div class="feat box" style="top:30px">Ratio 16:9</div>
  <div class="feat box" style="top:51px">Full HD</div>
  <div class="feat box" style="top:73px">Custom color pallet</div>
  <div class="feat box" style="top:94px">Custom Font -&nbsp; Easy Change</div>
  <div class="feat sub" style="top:115px">Monserat Bold</div>
  <div class="feat sub light" style="top:137px">Opens Sans</div>
  <div class="feat box" style="top:158px">Easy to edit, just drag and</div>
  <div class="feat" style="top:179px;left:54px">drop images</div>
  <div class="feat box" style="top:200px">Can be included up to 100</div>
  <div class="feat cont" style="top:219px">slides;</div>
  <div class="feat sub2" style="top:240px">Text + images (1,2,3,4)</div>
  <div class="feat sub2" style="top:262px">Portfolio Slides</div>
  <div class="feat sub2" style="top:283px">Text Slides</div>
  <div class="feat sub2" style="top:304px">Infografics</div>
  <div class="feat box" style="top:325px">In the sample load you will</div>
  <div class="feat cont" style="top:344px">find 19 slides</div>
</div>

<section class="cover" aria-label="Title slide">
  <div class="cover-top" role="img" aria-label="Photo of business people talking in a bright office"></div>
  <div class="cover-band"></div>
  <div class="cover-name">VELMIQ</div>
  <div class="cover-bottom" role="img" aria-label="Photo of printed bar charts on a desk"></div>
</section>

<!-- Agenda -->
<section class="slide r1 c1">
  <div class="brand">VELMIQ</div>
  <div class="tick"></div>
  <div class="title" style="left:20px;top:23px;font-size:23px;color:var(--blue)">Agenda</div>
  <div class="photo warm" role="img" aria-label="Photo of a person working at a desk" style="left:38px;top:36px;width:57px;height:43px"></div>
  <div class="agenda-band"></div>
  <div class="agenda-num" style="left:41px">01</div>
  <div class="agenda-num" style="left:97px">02</div>
  <div class="agenda-num" style="left:153px">03</div>
  <div class="col-head" style="left:40px;top:90px">Overview</div>
  <div class="col-head" style="left:97px;top:90px">Meet our team</div>
  <div class="col-head" style="left:153px;top:90px">Meet our Solution</div>
  <p class="para" style="left:40px;top:99px;width:52px">A short note on goals and scope.</p>
  <p class="para" style="left:97px;top:99px;width:52px"><b>A short note on our people</b> and the roles they hold across each project.</p>
  <p class="para" style="left:153px;top:99px;width:55px">How we plan, build and deliver for each client.</p>
  <div class="pg">2</div>
</section>

<!-- Welcome -->
<section class="slide r1 c2">
  <div class="brand">VELMIQ</div>
  <div class="tick"></div>
  <div class="photo" role="img" aria-label="Photo of hands over a tablet and charts" style="left:17px;top:0;width:57px;height:127px"></div>
  <div class="navy-block" style="left:55px;top:64px;width:19px;height:42px"><div class="arrow"></div></div>
  <div class="title" style="left:94px;top:31px;font-size:11px"><span class="hl">Welcome</span><br>Message</div>
  <p class="para" style="left:94px;top:62px;width:108px;font-size:3.6px"><b>A note from our team on why we work the way we do</b> and what you can expect from us on each project, from start to finish.</p>
  <div class="pg">3</div>
</section>

<!-- About -->
<section class="slide r1 c3">
  <div class="brand">VELMIQ</div>
  <div class="tick"></div>
  <div class="photo blue" role="img" aria-label="Photo of a hand holding a phone over printed charts" style="left:20px;top:0;width:56px;height:127px"></div>
  <div class="title" style="left:95px;top:19px;font-size:11px">About us</div>
  <div class="subtitle" style="left:95px;top:43px">Subtitle</div>
  <p class="para" style="left:95px;top:52px;width:104px"><b>We are a small team of advisers</b> who help banks, developers and builders plan, fund and run large projects with clear data and steady reports.</p>
  <p class="para" style="left:95px;top:76px;width:104px">Each review sets out risks, costs and timing so leaders can act with confidence.</p>
  <p class="para" style="left:95px;top:92px;width:104px">We stay with each client from first study to final handover.</p>
  <div class="navy-block" style="left:208px;top:43px;width:18px;height:41px"><div class="arrow"></div></div>
  <div class="pg">4</div>
</section>

<!-- Our Service -->
<section class="slide r2 c1">
  <div class="brand left">VELMIQ</div>
  <div class="tick"></div>
  <div class="title" style="left:21px;top:28px;font-size:10.5px">Our<br><span class="hl">Service</span></div>
  <div class="subtitle" style="left:21px;top:59px">Subtitle</div>
  <p class="para" style="left:21px;top:67px;width:52px"><b>We plan and review each project</b> with clear reports and steady advice.</p>
  <div class="photo warm" role="img" aria-label="Photo of a team at a meeting table" style="left:94px;top:0;width:57px;height:39px"></div>
  <div class="photo" role="img" aria-label="Photo of documents and a laptop" style="left:86px;top:41px;width:57px;height:43px"></div>
  <div class="photo dark" role="img" aria-label="Photo of a construction site with workers" style="left:94px;top:86px;width:57px;height:41px"></div>
  <div class="subtitle" style="left:160px;top:7px">Subtitle here</div>
  <p class="para" style="left:160px;top:15px;width:52px"><b>A short note on this service</b> and what it brings.</p>
  <div class="subtitle" style="left:154px;top:47px">Subtitle here</div>
  <p class="para" style="left:154px;top:55px;width:48px"><b>A short note on this service</b> and what it brings.</p>
  <div class="navy-block" style="left:207px;top:41px;width:19px;height:43px"></div>
  <div class="subtitle" style="left:161px;top:91px">Subtitle here</div>
  <p class="para" style="left:161px;top:99px;width:52px"><b>A short note on this service</b> and what it brings.</p>
  <div class="pg">5</div>
</section>

<!-- Timeline -->
<section class="slide r2 c2">
  <div class="brand">VELMIQ</div>
  <div class="tick"></div>
  <div class="title" style="left:29px;top:20px;font-size:11px">Timeline</div>
  <div class="circle" style="left:37px;top:51px;width:38px;height:38px"><span class="yr">2006</span><span class="note">Firm founded with a small team.</span></div>
  <div class="circle" style="left:124px;top:51px;width:38px;height:38px"><span class="yr">2012</span><span class="note">First bank client for audits.</span></div>
  <div class="circle" style="left:167px;top:51px;width:38px;height:38px"><span class="yr">2019</span><span class="note">Offices opened in two regions.</span></div>
  <div class="photo dark" role="img" aria-label="Round photo of a port with cranes" style="left:64px;top:36px;width:72px;height:72px;border-radius:50%"></div>
  <div class="circle" style="left:82px;top:54px;width:36px;height:36px;background:var(--navy);color:#fff"><span class="yr" style="margin-top:10px">2010</span><span class="note" style="color:#cfe0f0">Growth into major build work.</span></div>
  <div class="pg">6</div>
</section>

<!-- Knowing the Problem -->
<section class="slide r2 c3">
  <div class="brand">VELMIQ</div>
  <div class="tick"></div>
  <div class="title" style="left:38px;top:20px;font-size:12.5px">Knowing <span class="hl">the Problem</span></div>
  <div class="subtitle" style="left:38px;top:42px;font-size:3.5px">Subtitle</div>
  <p class="para" style="left:38px;top:49px;width:168px;font-size:2.4px"><b>Large projects slip when costs, risks and timing are not tracked in one place.</b> Owners get late reports, lenders lack clear data and teams act on guesswork rather than facts.</p>
  <p class="para" style="left:38px;top:60px;width:168px;font-size:2.4px">Our first step is to map each gap in the current process, from early budgets to site reports, and show where time and money are lost. We then rank each issue by its cost and its effect on the wider program so that leaders can see what to fix first.</p>
  <p class="para" style="left:38px;top:78px;width:168px;font-size:2.4px">With this view in hand, the board can set clear targets, agree on owners for each task and follow progress through short, regular reports that show real numbers rather than loose estimates.</p>
  <p class="para" style="left:38px;top:94px;width:168px;font-size:2.4px">The result is a plan everyone can read and trust.</p>
  <div class="pg">7</div>
</section>

<!-- The Solution -->
<section class="slide r3 c1">
  <div class="brand">VELMIQ</div>
  <div class="tick"></div>
  <div class="title" style="left:38px;top:20px;font-size:12px">The <span class="hl">Solution</span></div>
  <p class="para" style="left:38px;top:41px;width:52px;font-size:2.4px"><b>A single plan for cost, risk and time</b> shared by owners, lenders and builders so each party reads the same figures.</p>
  <p class="para" style="left:97px;top:41px;width:52px;font-size:2.4px">Regular site reviews keep the data fresh and flag any slip early, before it grows into a costly delay.</p>
  <p class="para" style="left:157px;top:41px;width:52px;font-size:2.4px">Clear monthly reports give the board a short view of progress and the steps that come next.</p>
  <div class="photo dark" role="img" aria-label="Photo of two business people shaking hands" style="left:19px;top:84px;width:207px;height:43px"></div>
  <div class="pg">8</div>
</section>

<!-- Left Strategy -->
<section class="slide r3 c2">
  <div class="brand">VELMIQ</div>
  <div class="tick"></div>
  <div class="strat-box" style="left:19px;top:21px"><h4>Strategy One</h4><p><b>Set clear goals</b> and agree on the scope.</p></div>
  <div class="strat-box" style="left:68px;top:21px"><h4>Strategy Two</h4><p><b>Map each risk</b> and assign an owner.</p></div>
  <div class="strat-box" style="left:19px;top:70px"><h4>Strategy Three</h4><p><b>Track cost</b> and timing every month.</p></div>
  <div class="strat-box" style="left:68px;top:70px"><h4>Strategy Four</h4><p><b>Report early</b> and act on the facts.</p></div>
  <div class="title" style="left:131px;top:19px;font-size:10.5px"><span class="hl">Left</span><br>Strategy<br>in box text</div>
  <div class="subtitle" style="left:131px;top:63px">Subtitle</div>
  <p class="para" style="left:131px;top:72px;width:66px"><b>Four steps that keep each project on track</b> from first study to final handover, with clear owners and short reports at every stage.</p>
  <div class="pg">9</div>
</section>

<!-- Right Strategy -->
<section class="slide r3 c3">
  <div class="brand">VELMIQ</div>
  <div class="tick"></div>
  <div class="title" style="left:38px;top:19px;font-size:10.5px"><span class="hl">Right</span><br>Strategy<br>icon + text</div>
  <div class="subtitle" style="left:38px;top:59px">Subtitle</div>
  <p class="para" style="left:38px;top:67px;width:64px"><b>Four tools we use</b> on every project to keep cost, risk and time in view.</p>
  <p class="para" style="left:38px;top:86px;width:64px">Each one feeds a short report for the board.</p>
  <div class="icon-box" style="left:113px;top:21px">
    <svg width="8" height="8" viewBox="0 0 16 16" fill="none" stroke="#555" stroke-width="1.2"><path d="M2 2h12l-5 6v5l-2 1V8z"/></svg>
    <h4>Subtitle here</h4><p>Filter key risks</p>
  </div>
  <div class="icon-box" style="left:162px;top:21px">
    <svg width="8" height="8" viewBox="0 0 16 16" fill="none" stroke="#555" stroke-width="1.2"><rect x="1.5" y="3" width="13" height="10"/><path d="M1.5 6h13M4 9h2M8 9h2M12 9h1"/></svg>
    <h4>Subtitle here</h4><p>Plan each budget</p>
  </div>
  <div class="icon-box" style="left:113px;top:70px">
    <svg width="8" height="8" viewBox="0 0 16 16" fill="none" stroke="#555" stroke-width="1.2"><circle cx="8" cy="8" r="2.5"/><circle cx="8" cy="8" r="6"/></svg>
    <h4>Subtitle here</h4><p>Set up the process</p>
  </div>
  <div class="icon-box" style="left:162px;top:70px">
    <svg width="8" height="8" viewBox="0 0 16 16" fill="none" stroke="#555" stroke-width="1.2"><path d="M15 1L1 7l6 2 2 6z"/></svg>
    <h4>Subtitle here</h4><p>Send clear reports</p>
  </div>
  <div class="pg">10</div>
</section>

<!-- Problem Analysis -->
<section class="slide r4 c1">
  <div class="brand left">VELMIQ</div>
  <div class="tick"></div>
  <div class="title" style="left:21px;top:28px;font-size:11px">Problem <span class="hl">Analysis</span></div>
  <p class="para" style="left:21px;top:45px;width:82px;font-size:2.4px"><b>Where the main delays come from</b> across recent projects, ranked by the share of cost overrun each one caused in the last review.</p>
  <div class="meter" style="top:74px"><span style="width:57px">Element One</span><em style="left:44px">75%</em></div>
  <div class="meter active" style="top:88px"><span style="width:38px">Element Two</span><em style="left:26px">50%</em></div>
  <div class="meter" style="top:102px"><span style="width:68px">Element Three</span><em style="left:57px">90%</em></div>
  <div class="photo blue" role="img" aria-label="Photo of a blue 3D pie chart" style="left:132px;top:0;width:94px;height:127px"></div>
  <div class="pg">11</div>
</section>

<!-- Portfolio -->
<section class="slide r4 c2">
  <div class="brand">VELMIQ</div>
  <div class="tick"></div>
  <div class="title" style="left:38px;top:20px;font-size:10.5px">Our Projects<br><span class="hl">Portfolio</span></div>
  <div class="photo" role="img" aria-label="Project photo: charts on a desk" style="left:37px;top:51px;width:37px;height:37px"></div>
  <div class="photo dark" role="img" aria-label="Project photo: construction site" style="left:75px;top:51px;width:37px;height:37px"></div>
  <div class="photo warm" role="img" aria-label="Project photo: hands with documents" style="left:113px;top:51px;width:37px;height:37px"></div>
  <div class="photo blue" role="img" aria-label="Project photo: business people in an office" style="left:151px;top:51px;width:37px;height:37px"></div>
  <div class="photo" role="img" aria-label="Project photo: person at a laptop" style="left:189px;top:51px;width:37px;height:37px"></div>
  <div class="photo warm" role="img" aria-label="Project photo: person writing notes" style="left:37px;top:89px;width:37px;height:38px"></div>
  <div class="photo blue" role="img" aria-label="Project photo: office desk with screens" style="left:75px;top:89px;width:37px;height:38px"></div>
  <div class="photo" role="img" aria-label="Project photo: tablet with a chart" style="left:113px;top:89px;width:37px;height:38px"></div>
  <div class="photo blue" role="img" aria-label="Project photo: printed reports" style="left:151px;top:89px;width:37px;height:38px"></div>
  <div class="photo dark" role="img" aria-label="Project photo: man at a computer" style="left:189px;top:89px;width:37px;height:38px"></div>
  <div class="pg">12</div>
</section>

<!-- Meet the Team cover -->
<section class="slide r4 c3">
  <div class="brand left">VELMIQ</div>
  <div class="tick"></div>
  <div class="photo" role="img" aria-label="Photo of a smiling team in a bright office" style="left:113px;top:0;width:113px;height:127px;background:linear-gradient(135deg,#eef1f5,#aab6c4)"></div>
  <div class="title" style="left:57px;top:55px;font-size:16px">Meet <span class="hl">the Team</span></div>
  <div class="pg">13</div>
</section>

<!-- Meet the Team -->
<section class="slide r5 c1">
  <div class="brand">VELMIQ</div>
  <div class="tick"></div>
  <div class="title" style="left:51px;top:21px;font-size:12px">Meet <span class="hl">the Team</span></div>
  <div class="member" style="left:33px"><div class="portrait" role="img" aria-label="Portrait photo of a team member"></div><div class="name">John Doe</div><div class="role">Graphic Designer</div></div>
  <div class="member lead" style="left:74px"><div class="portrait" role="img" aria-label="Portrait photo of the CEO"></div><div class="caption"><div class="name">John Doe</div><div class="role">CEO</div></div></div>
  <div class="member" style="left:116px"><div class="portrait" role="img" aria-label="Portrait photo of a team member"></div><div class="name">John Doe</div><div class="role">Graphic Designer</div></div>
  <div class="member" style="left:158px"><div class="portrait" role="img" aria-label="Portrait photo of a team member"></div><div class="name">John Doe</div><div class="role">Graphic Designer</div></div>
  <div class="pg">14</div>
</section>

<!-- Data Chart -->
<section class="slide r5 c2">
  <div class="brand left">VELMIQ</div>
  <div class="tick"></div>
  <div class="photo dark" role="img" aria-label="Photo of a pen over a printed line chart" style="left:113px;top:0;width:113px;height:127px"></div>
  <div class="title" style="left:67px;top:55px;font-size:16px"><span class="hl">Data</span>&nbsp; <span style="color:#fff">Chart</span></div>
  <div class="pg">15</div>
</section>

<!-- Clustered Chart -->
<section class="slide r5 c3">
  <div class="brand">VELMIQ</div>
  <div class="tick"></div>
  <div class="title" style="left:28px;top:21px;font-size:10.5px">Clustered<br><span class="hl">Chart Style</span></div>
  <div class="subtitle" style="left:28px;top:52px;font-size:3.5px">Subtitle</div>
  <p class="para" style="left:28px;top:58px;width:44px;font-size:2.4px"><b>Spend by quarter</b> across three project groups, in millions.</p>
  <p class="para" style="left:28px;top:74px;width:44px;font-size:2.4px">Group three shows the largest rise in the last period.</p>
  <svg style="position:absolute;left:95px;top:24px" width="112" height="84" viewBox="0 0 112 84">
    <g font-family="Open Sans" font-size="2.2" fill="#888">
      <rect x="34" y="0" width="3" height="1.5" fill="var(--bar-a)"/><text x="38" y="1.6">Series 1</text>
      <rect x="50" y="0" width="3" height="1.5" fill="var(--bar-b)"/><text x="54" y="1.6">Series 2</text>
      <rect x="66" y="0" width="3" height="1.5" fill="var(--bar-c)"/><text x="70" y="1.6">Series 3</text>
      <text x="0" y="12">6</text><text x="0" y="24">5</text><text x="0" y="36">4</text><text x="0" y="48">3</text><text x="0" y="60">2</text><text x="0" y="72">1</text><text x="0" y="84">0</text>
    </g>
    <line x1="5" y1="80" x2="112" y2="80" stroke="#ccc" stroke-width=".4"/>
    <g>
      <rect x="10" y="28" width="5" height="52" fill="var(--bar-a)"/><rect x="15" y="51" width="5" height="29" fill="var(--bar-b)"/><rect x="20" y="56" width="5" height="24" fill="var(--bar-a)"/>
      <rect x="36" y="50" width="5" height="30" fill="var(--bar-a)"/><rect x="41" y="27" width="5" height="53" fill="var(--bar-b)"/><rect x="46" y="56" width="5" height="24" fill="var(--bar-a)"/>
      <rect x="62" y="38" width="5" height="42" fill="var(--bar-a)"/><rect x="67" y="58" width="5" height="22" fill="var(--bar-b)"/><rect x="72" y="44" width="5" height="36" fill="var(--bar-a)"/>
      <rect x="88" y="26" width="5" height="54" fill="var(--bar-a)"/><rect x="93" y="46" width="5" height="34" fill="var(--bar-b)"/><rect x="98" y="20" width="5" height="60" fill="var(--bar-a)"/>
    </g>
    <g font-family="Open Sans" font-size="2" fill="#888">
      <text x="12" y="83.5">Category 1</text><text x="38" y="83.5">Category 2</text><text x="64" y="83.5">Category 3</text><text x="90" y="83.5">Category 4</text>
    </g>
  </svg>
  <div class="pg">16</div>
</section>

<!-- Clustered Bar -->
<section class="slide r6 c1">
  <div class="brand">VELMIQ</div>
  <div class="tick"></div>
  <div class="title" style="left:28px;top:20px;font-size:10.5px"><span class="hl">Clustered</span><br>Bar Style</div>
  <div class="subtitle" style="left:28px;top:51px;font-size:3.5px">Subtitle</div>
  <p class="para" style="left:28px;top:57px;width:44px;font-size:2.4px"><b>Hours per task type</b> across three teams over the last quarter.</p>
  <p class="para" style="left:28px;top:73px;width:44px;font-size:2.4px">Team two spent the most time on site checks.</p>
  <svg style="position:absolute;left:96px;top:22px" width="112" height="88" viewBox="0 0 112 88">
    <g font-family="Open Sans" font-size="2.2" fill="#888">
      <rect x="30" y="0" width="3" height="1.5" fill="var(--bar-a)"/><text x="34" y="1.6">Series 3</text>
      <rect x="46" y="0" width="3" height="1.5" fill="var(--bar-b)"/><text x="50" y="1.6">Series 2</text>
      <rect x="62" y="0" width="3" height="1.5" fill="var(--bar-a)"/><text x="66" y="1.6">Series 1</text>
    </g>
    <line x1="10" y1="6" x2="10" y2="82" stroke="#ccc" stroke-width=".4"/>
    <g>
      <rect x="10" y="9" width="86" height="3" fill="var(--bar-a)"/><rect x="10" y="12" width="52" height="3" fill="var(--bar-b)"/><rect x="10" y="15" width="76" height="3" fill="var(--bar-a)"/>
      <rect x="10" y="27" width="52" height="3" fill="var(--bar-a)"/><rect x="10" y="30" width="30" height="3" fill="var(--bar-b)"/><rect x="10" y="33" width="60" height="3" fill="var(--bar-a)"/>
      <rect x="10" y="45" width="34" height="3" fill="var(--bar-a)"/><rect x="10" y="48" width="76" height="3" fill="var(--bar-b)"/><rect x="10" y="51" width="42" height="3" fill="var(--bar-a)"/>
      <rect x="10" y="63" width="50" height="3" fill="var(--bar-a)"/><rect x="10" y="66" width="42" height="3" fill="var(--bar-b)"/><rect x="10" y="69" width="76" height="3" fill="var(--bar-a)"/>
    </g>
    <g font-family="Open Sans" font-size="2" fill="#888">
      <text x="1" y="14">Cat 1</text><text x="1" y="32">Cat 2</text><text x="1" y="50">Cat 3</text><text x="1" y="68">Cat 4</text>
      <text x="9" y="86">0</text><text x="26" y="86">1</text><text x="43" y="86">2</text><text x="60" y="86">3</text><text x="77" y="86">4</text><text x="94" y="86">5</text><text x="109" y="86">6</text>
    </g>
  </svg>
  <div class="pg">17</div>
</section>

<!-- Pie Chart -->
<section class="slide r6 c2">
  <div class="brand">VELMIQ</div>
  <div class="tick"></div>
  <div class="title" style="left:29px;top:21px;font-size:10.5px"><span class="hl">Pie Chart</span><br>Style</div>
  <div class="subtitle" style="left:29px;top:52px;font-size:3.5px">Subtitle</div>
  <p class="para" style="left:29px;top:58px;width:44px;font-size:2.4px"><b>Budget share</b> by work stream for the current program year.</p>
  <p class="para" style="left:29px;top:74px;width:44px;font-size:2.4px">Design and site work take over half of all spend.</p>
  <svg style="position:absolute;left:98px;top:12px" width="110" height="110" viewBox="0 0 110 110">
    <text x="48" y="6" font-family="Open Sans" font-size="2.6" fill="#666">Series 1</text>
    <g transform="translate(54 58) scale(1 .72)">
      <g transform="translate(0 9)">
        <circle r="48" fill="#2a2a2e"/>
      </g>
      <path d="M0 0 L0 -48 A48 48 0 0 1 46.3 12.6 Z" fill="var(--bar-a)"/>
      <path d="M0 0 L46.3 12.6 A48 48 0 0 1 15.2 45.5 Z" fill="var(--bar-c)"/>
      <path d="M0 0 L15.2 45.5 A48 48 0 0 1 -45.9 13.8 Z" fill="var(--bar-b)"/>
      <path d="M0 0 L-45.9 13.8 A48 48 0 0 1 -2 -48 Z" fill="#2e6fad"/>
    </g>
    <g font-family="Open Sans" font-size="2.2" fill="#fff">
      <text x="70" y="42">Category 1</text><text x="72" y="45">29%</text>
      <text x="76" y="70">Category 2</text><text x="78" y="73">17%</text>
      <text x="40" y="80">Category 3</text><text x="42" y="83">24%</text>
      <text x="22" y="48">Category 4</text><text x="24" y="51">30%</text>
    </g>
  </svg>
  <div class="pg">18</div>
</section>

<!-- Area Chart -->
<section class="slide r6 c3">
  <div class="brand">VELMIQ</div>
  <div class="tick"></div>
  <div class="title" style="left:28px;top:21px;font-size:10.5px"><span class="hl">Area Chart</span><br>Style</div>
  <div class="subtitle" style="left:28px;top:52px;font-size:3.5px">Subtitle</div>
  <p class="para" style="left:28px;top:58px;width:44px;font-size:2.4px"><b>Progress rate</b> for three sites measured over ten weeks.</p>
  <p class="para" style="left:28px;top:74px;width:44px;font-size:2.4px">Site one recovered after a slow start.</p>
  <svg style="position:absolute;left:98px;top:22px" width="112" height="88" viewBox="0 0 112 88">
    <g font-family="Open Sans" font-size="2.2" fill="#888">
      <line x1="32" y1="1" x2="36" y2="1" stroke="var(--bar-a)" stroke-width=".8"/><text x="37" y="1.8">Series 1</text>
      <line x1="48" y1="1" x2="52" y2="1" stroke="var(--bar-c)" stroke-width=".8"/><text x="53" y="1.8">Series 2</text>
      <line x1="64" y1="1" x2="68" y2="1" stroke="#5b8fd0" stroke-width=".8"/><text x="69" y="1.8">Series 3</text>
      <text x="0" y="10">6</text><text x="0" y="22">5</text><text x="0" y="34">4</text><text x="0" y="46">3</text><text x="0" y="58">2</text><text x="0" y="70">1</text><text x="0" y="82">0</text>
      <text x="4" y="86">0</text><text x="16" y="86">0.5</text><text x="28" y="86">1</text><text x="40" y="86">1.5</text><text x="52" y="86">2</text><text x="64" y="86">2.5</text><text x="76" y="86">3</text><text x="88" y="86">3.5</text><text x="100" y="86">4</text>
    </g>
    <g fill="none" stroke-width=".8">
      <path d="M28 44 C40 70 48 30 58 40 S78 66 86 62 S100 46 104 30" stroke="var(--bar-a)"/>
      <path d="M28 56 C40 58 60 52 72 58 S92 40 104 30" stroke="var(--bar-c)"/>
      <path d="M28 60 C36 40 48 44 56 58 S76 50 90 40 S100 32 104 28" stroke="#5b8fd0"/>
    </g>
  </svg>
  <div class="pg">19</div>
</section>

</body>
</html>
```